Award-winnning Estate Agent needs a premium version of their 'For Sale' board design

We need a premium option for our 'For Sale' board design. We have a standard board that is attached to this brief, but were are looking to have a premium design version that we will use when selling exclusive properties. Our company name is Harbour Lane Estates and the name for this is exclusive selection is: 'The Harbour Collection'. The design needs to work with our current brand, but have a distinctive PREMIUM feel to it. I have uploaded the barnd guidelines and also some of the exisisting logo variations. We do NOT need a new logo but feel free to play around with colours, fonts, sizes etc. for the sign.

Target Market(s)

Property buyers & house hunters

Industry/Entity Type

Real Estate - Residential Property

Font styles to use
Sans Serif

Requirements
Must have
• A premium fee, must be square design, must be easy to read when driving past the sign
Nice to have
• I'm open ot ideas

```html
<!DOCTYPE html>
<html lang="en">
<head>
<meta charset="utf-8">
<title>Harbour Lane Estates – The Harbour Collection For Sale Board</title>
<link href="https://fonts.googleapis.com/css2?family=Outfit:wght@300;400;600;700&display=swap" rel="stylesheet">
<style>
  :root {
    --board-white: #ffffff;
    --brand-blue: #0e72b8;
    --brand-purple: #432c73;
    --sale-text: #cce4fa;
    --ink: #0b0b0b;
    --bracket: #4a6aa8;
  }
  html, body {
    margin: 0;
    padding: 0;
    width: 1200px;
    height: 1200px;
    overflow: hidden;
    background: var(--board-white);
  }
  .sale-board {
    display: block;
    width: 1200px;
    height: 1200px;
    font-family: "Outfit", sans-serif;
  }
  .frame { fill: none; stroke: var(--brand-blue); stroke-width: 3; }
  .frame-inner { fill: none; stroke: var(--brand-purple); stroke-width: 1; }
  .frame-break { stroke: var(--board-white); stroke-width: 3; }
  .sale-band { fill: var(--brand-blue); }
  .brand-mark { fill: var(--brand-purple); }
  .brand-name { fill: var(--brand-purple); font-weight: 600; font-size: 84px; }
  .collection-rule { stroke: var(--brand-purple); stroke-width: 2; }
  .collection-name { fill: var(--brand-purple); font-weight: 400; font-size: 40px; letter-spacing: 9px; }
  .sale-title { fill: var(--sale-text); font-weight: 600; font-size: 218px; }
  .phone-number { fill: var(--ink); font-weight: 700; font-size: 152px; }
  .contact-bracket { fill: none; stroke: var(--bracket); stroke-width: 2; }
  .web-address { fill: var(--brand-blue); font-size: 60px; }
  .web-light { font-weight: 300; }
  .web-bold { font-weight: 700; }
</style>
</head>
<body>
<svg class="sale-board" viewBox="0 0 1200 1200" xmlns="http://www.w3.org/2000/svg">
  <rect class="frame" x="35" y="35" width="1129" height="1129"/>
  <rect class="frame-inner" x="48" y="48" width="1103" height="1103"/>

  <g class="collection">
    <line class="collection-rule" x1="150" y1="300" x2="250" y2="300"/>
    <text class="collection-name" x="600" y="314" text-anchor="middle" textLength="680" lengthAdjust="spacingAndGlyphs">THE HARBOUR COLLECTION</text>
    <line class="collection-rule" x1="950" y1="300" x2="1050" y2="300"/>
  </g>

  <g class="brand">
    <rect class="brand-mark" x="163" y="425" width="56" height="56"/>
    <text class="brand-name" x="240" y="483" textLength="800" lengthAdjust="spacingAndGlyphs">Harbour Lane Estates</text>
  </g>

  <rect class="sale-band" x="0" y="542" width="1200" height="240"/>
  <line class="frame-break" x1="36" y1="548" x2="36" y2="776"/>
  <line class="frame-break" x1="1163" y1="548" x2="1163" y2="776"/>
  <text class="sale-title" x="600" y="739" text-anchor="middle" textLength="938" lengthAdjust="spacingAndGlyphs">FOR SALE</text>

  <polyline class="contact-bracket" points="166,921 133,921 133,1081 1050,1081 1050,921 1017,921"/>
  <text class="phone-number" x="593" y="975" text-anchor="middle" textLength="823" lengthAdjust="spacingAndGlyphs">01632 960514</text>
  <text class="web-address" x="601" y="1047" text-anchor="middle" textLength="805" lengthAdjust="spacingAndGlyphs"><tspan class="web-light">www.</tspan><tspan class="web-bold">harbourlaneestates</tspan><tspan class="web-light">.co.uk</tspan></text>
</svg>
</body>
</html>
```